Landing page for Cloud Kitchen buisnies

We need a landing page design fully functional for our Cloud Kitchen company wich is based in Dubai we have a industrial kitchen setup up from where we operate our own online food brands wich are only availble for delivery

Target Market(s)

Its just a company Profile

Requirements
Must have
• Company name is Saffron Lane Group. We have the Logo already

LOGO AND DOMAIN WE HAVE
Nice to have
• Proffesionel high quality design

```html
<!DOCTYPE html>
<html lang="en">
<head>
<meta charset="UTF-8">
<title>Saffron Lane Group — Cloud Kitchen</title>
<link rel="stylesheet" href="https://fonts.googleapis.com/css2?family=Open+Sans:wght@300;400;600;700&display=swap">
<style>
  :root {
    --night: #0a0f18;
    --gold: #e2c158;
    --gold-deep: #b8892c;
    --gold-light: #f2e27e;
    --page-top: #f7f7f7;
    --page-bottom: #ebebeb;
    --ink: #3a3a3a;
    --white: #ffffff;
  }
  * { margin: 0; padding: 0; box-sizing: border-box; }
  html, body { width: 932px; height: 1200px; overflow: hidden; }
  body {
    position: relative;
    font-family: "Open Sans", sans-serif;
    background: linear-gradient(180deg, var(--white) 0%, var(--page-top) 40%, var(--page-bottom) 100%);
  }
  .hero-band {
    position: absolute; left: 0; top: 0; width: 654px; height: 466px;
    background: var(--night);
  }
  .brand {
    position: absolute; left: 128px; top: 40px;
    display: flex; align-items: center; gap: 8px;
    color: var(--gold); font-weight: 600; font-size: 15px; letter-spacing: 1px;
    line-height: 1.15;
  }
  .brand-dot { width: 14px; height: 14px; border-radius: 50%; background: var(--gold); flex: none; }
  .nav { position: absolute; top: 45px; left: 0; }
  .nav a {
    position: absolute; white-space: nowrap; text-decoration: none;
    color: var(--gold-deep); font-size: 9.5px; font-weight: 600; letter-spacing: 1px;
  }
  .contact-btn {
    position: absolute; left: 731px; top: 37px; width: 120px; height: 30px;
    border-radius: 15px; display: flex; align-items: center; justify-content: center;
    background: linear-gradient(90deg, var(--gold-deep), var(--gold-light));
    color: var(--white); font-size: 9.5px; font-weight: 600; letter-spacing: 1px;
    box-shadow: 0 4px 10px rgba(0,0,0,0.12); text-decoration: none;
  }
  .hero-title {
    position: absolute; left: 128px; top: 198px; width: 272px;
    color: var(--gold); font-size: 15.5px; font-weight: 600; line-height: 19px; letter-spacing: 0.6px;
  }
  .hero-text {
    position: absolute; left: 128px; top: 237px; width: 260px;
    color: var(--white); font-size: 9.2px; line-height: 11.7px; text-align: justify; letter-spacing: 0.6px;
  }
  .hero-visual { position: absolute; left: 386px; top: 172px; }
  .about-title {
    position: absolute; left: 0; width: 932px; top: 548px; text-align: center;
    color: var(--gold); font-size: 33px; font-weight: 700; letter-spacing: 2px;
  }
  .about-sub {
    position: absolute; left: 276px; width: 382px; top: 595px;
    display: flex; align-items: center; gap: 14px;
    color: var(--gold); font-size: 20px; font-weight: 300; letter-spacing: 1px; white-space: nowrap;
  }
  .about-sub::before, .about-sub::after { content: ""; flex: 1; height: 1px; background: var(--gold-deep); }
  .about-text {
    position: absolute; left: 173px; width: 587px; top: 647px;
    color: var(--ink); font-size: 9.3px; line-height: 11.7px; text-align: justify; text-align-last: center; letter-spacing: 0.4px;
  }
  .offerings-title {
    position: absolute; left: 101px; top: 766px;
    color: var(--gold); font-size: 33px; font-weight: 700; letter-spacing: 2px;
  }
  .offerings-rule { position: absolute; left: 103px; top: 812px; width: 274px; height: 1px; background: var(--gold-deep); }
  .offer { position: absolute; top: 862px; width: 182px; }
  .offer-art { width: 124px; height: 100px; margin: 0 auto; border-radius: 50px 50px 14px 14px;
    background: linear-gradient(135deg, var(--gold-light), var(--gold-deep)); opacity: 0.85; }
  .offer-name {
    position: relative; margin-top: 22px; padding-left: 2px; text-align: center;
    color: var(--gold); font-size: 13px; font-weight: 600; letter-spacing: 0.8px;
  }
  .offer-name::before { content: ""; position: absolute; left: -2px; top: -6px; width: 1px; height: 18px; background: var(--gold-deep); opacity: 0.6; }
  .offer-text {
    margin-top: 2px; color: var(--ink); font-size: 9.2px; font-weight: 600; line-height: 11.6px;
    text-align: justify; text-align-last: center; letter-spacing: 0.3px;
  }
  .cloud-edge { position: absolute; left: 0; top: 1092px; }
</style>
</head>
<body>
  <header class="hero-band"></header>

  <div class="brand"><span class="brand-dot"></span><span>SAFFRON LANE<br>GROUP</span></div>

  <nav class="nav">
    <a href="#about" style="left:293px">ABOUT US</a>
    <a href="#offerings" style="left:402px">OUR OFFERINGS</a>
    <a href="#why" style="left:543px">WHY US</a>
  </nav>
  <a class="contact-btn" href="#contact">CONTACT US</a>

  <h1 class="hero-title">QUALITY COMMERCIAL KITCHEN OPTIMIZED FOR DELIVERY.</h1>
  <p class="hero-text">Lorem ipsum dolor sit amet, consectetur adipisicing elit, sed do eiusmod tempor incididunt ut labore et dolore magna aliqua. Ut enim ad minim veniam, quis nostrud exercitation ullamco laboris nisi ut aliquip ex ea commodo consequat. Duis aute irure dolor in reprehenderit in voluptate velit esse cillum dolore eu fugiat nulla pariatur. Excepteur sint occaecat cupidatat non proident, sunt in culpa qui officia deserunt mollit anim id est laborum.</p>

  <svg class="hero-visual" width="546" height="346" viewBox="0 0 546 346" role="img" aria-label="Photo of a chef working in a commercial kitchen, framed in a gold cloud shape">
    <defs>
      <linearGradient id="photoTone" x1="0" y1="0" x2="1" y2="1">
        <stop offset="0" stop-color="#6b625a"/>
        <stop offset="0.5" stop-color="#a69886"/>
        <stop offset="1" stop-color="#4a3f36"/>
      </linearGradient>
      <linearGradient id="goldFrame" x1="0" y1="1" x2="1" y2="0">
        <stop offset="0" stop-color="#b8892c"/>
        <stop offset="1" stop-color="#f2e27e"/>
      </linearGradient>
    </defs>
    <path d="M 120 324 C 40 318 8 270 14 228 C 20 186 56 160 96 162 C 100 70 150 8 232 10 C 300 12 340 40 356 84 C 390 60 452 58 484 96 C 504 120 510 146 506 172 C 538 196 546 250 524 290 C 506 320 478 328 456 326 L 436 340 L 440 322 Z"
          fill="url(#photoTone)" stroke="url(#goldFrame)" stroke-width="16" stroke-linejoin="round"/>
    <path d="M 96 346 C 92 300 130 252 190 238 C 240 228 280 238 300 254 C 340 240 400 252 440 290 L 452 346 Z"
          fill="#f6f6f6"/>
    <path d="M 96 346 C 92 300 130 252 190 238 C 240 228 280 238 300 254 C 340 240 400 252 440 290"
          fill="none" stroke="url(#goldFrame)" stroke-width="14" stroke-linecap="round"/>
  </svg>

  <h2 class="about-title" id="about">WHAT IS SAFFRON LANE</h2>
  <div class="about-sub">ABOUT US</div>
  <p class="about-text">Lorem ipsum dolor sit amet, consectetur adipisicing elit, sed do eiusmod tempor incididunt ut labore et dolore magna aliqua. Ut enim ad minim veniam, quis nostrud exercitation ullamco laboris nisi ut aliquip ex ea commodo consequat. Duis aute irure dolor in reprehenderit in voluptate velit esse cillum dolore eu fugiat nulla pariatur. Excepteur sint occaecat cupidatat non proident, sunt in culpa qui officia deserunt mollit anim id est laborum.</p>

  <h2 class="offerings-title" id="offerings">OUR OFFERINGS</h2>
  <div class="offerings-rule"></div>

  <section class="offer" style="left:99px">
    <div class="offer-art" role="img" aria-label="Illustration of a person ordering food on a tablet"></div>
    <h3 class="offer-name">LOREM IPSUM</h3>
    <p class="offer-text">Lorem ipsum dolor sit amet, consectetur adipiscing elit, sed do eiusmod tempor incididunt ut labore et dolore magna aliqua. Quis ipsum suspendisse ultrices gravida.</p>
  </section>
  <section class="offer" style="left:375px">
    <div class="offer-art" role="img" aria-label="Illustration of a serving cloche surrounded by food icons"></div>
    <h3 class="offer-name">LOREM IPSUM</h3>
    <p class="offer-text">Lorem ipsum dolor sit amet, consectetur adipiscing elit, sed do eiusmod tempor incididunt ut labore et dolore magna aliqua. Quis ipsum suspendisse ultrices gravida.</p>
  </section>
  <section class="offer" style="left:651px">
    <div class="offer-art" role="img" aria-label="Illustration of a delivery scooter carrying food"></div>
    <h3 class="offer-name">LOREM IPSUM</h3>
    <p class="offer-text">Lorem ipsum dolor sit amet, consectetur adipiscing elit, sed do eiusmod tempor incididunt ut labore et dolore magna aliqua. Quis ipsum suspendisse ultrices gravida.</p>
  </section>

  <svg class="cloud-edge" width="932" height="108" viewBox="0 0 932 108" aria-hidden="true">
    <g fill="#ffffff">
      <rect x="0" y="40" width="932" height="68"/>
      <circle cx="28" cy="32" r="28"/><circle cx="68" cy="44" r="22"/>
      <circle cx="117" cy="32" r="28"/><circle cx="157" cy="44" r="22"/>
      <circle cx="205" cy="32" r="28"/><circle cx="245" cy="44" r="22"/>
      <circle cx="294" cy="32" r="28"/><circle cx="334" cy="44" r="22"/>
      <circle cx="383" cy="32" r="28"/><circle cx="423" cy="44" r="22"/>
      <circle cx="471" cy="32" r="28"/><circle cx="511" cy="44" r="22"/>
      <circle cx="560" cy="32" r="28"/><circle cx="600" cy="44" r="22"/>
      <circle cx="649" cy="32" r="28"/><circle cx="689" cy="44" r="22"/>
      <circle cx="737" cy="32" r="28"/><circle cx="777" cy="44" r="22"/>
      <circle cx="826" cy="32" r="28"/><circle cx="866" cy="44" r="22"/>
      <circle cx="915" cy="32" r="28"/>
    </g>
  </svg>
</body>
</html>
```